Website design for an Online pastry shop

Website Name : www.lanternandplum.example

Description of the website and its target audience
We are a premium pastry company producing delicious cakes, macarons, cookies, gelato, and other sweet dessert. Our differentiation is that our products are freshly produced with premium quality imported ingredients and one bite into our products set us apart from other bakery shop. We online retail online so as to provide high quality products at a affordable cost. Our products has received raving reviews by many food enthusiast even the hard to please ones. The products contain more natural ingredients and we do not add preservatives. The return rates for our pastry is almost 80%. You only need to try once to be return customers. Our greatest challenge is getting customer to take the first bite. We are so sure of our products that we are going to give people free food tasting.

We are based in China but all our products are developed by award winning chefs from 5 stars hotel. The target customer is woman 16 to 40+ in china. Working class ladies and demand high quality products. A modern, sophisticated and minimalist website

This is a competitive market and image is crucial for such a food ‘conscious ’ orientated customer. They want to feel that they are buying from a reliable company that take great effort to ensure food cleaniness and safety yet affordable price. We make almost 98% of sub ingredients ourselves and we make it by hand.

Style/theme ideas for the web page design
I am looking for a elegant a little rustic, handmade feel yet sophisticated design - one that is easy to the eye yet functional and easy for the user to navigate through. Good play of fonts to give let it feel unique and customised. Black and white is our corporate colours. However, we do not want black background as it does not tease the taste bud. All our colours should come from our products. Customers should be very close to our products. They eat with their eyes first. Black and white is just accent.

Inspirational and competitors websites
http://www.47tart.example/ ( Key competitor )
I like the simple, clean look. The products are the key focus
https://www.pelvora.example/
clean, fresh and different. Attractive with purpose. Feminine
http://moatandwillow.example/
this has a great layout - lots of information and nicely presented. Very sweet and feminine
http://www.storeharbourly.example/
product features is the focus
http://www.janetobrill.example/store/
fun, feminine, rustic

Number of pages needed : 6 ( Uncoded PSD design only )
Page descriptions
Home Page - This page will show what makes our products stand out from the competitors and provide an introduction of who we are.
2nd page : Product catalogue
3nd page: Detail Product page with pictures and descriptions. Select products size and add to cart....
4rd page: Brand Story with pictures and descriptions.
5th page Contact Us : Here they can contact or schedule an appointment for free product tasting
6th page : Check out page

• Please see the project wire frame file " main page.png " or file number 70

```html
<!DOCTYPE html>
<html lang="en">
<head>
<meta charset="utf-8">
<title>Lantern &amp; Plum — Pastry Shop</title>
<link rel="stylesheet" href="https://fonts.googleapis.com/css2?family=Roboto+Slab:wght@400;700;800&family=Open+Sans:wght@400;600;700&family=Playfair+Display:ital,wght@1,400&display=swap">
<style>
:root{
  --ink:#222;
  --night:#1c1a19;
  --footer:#2b2928;
  --footer-text:#c9c4c0;
  --red:#c0201c;
  --red-dark:#9e1814;
  --grey:#6f6f6f;
  --light:#f3f1ef;
  --white:#fff;
}
*{box-sizing:border-box;margin:0;padding:0}
html,body{width:1200px;height:2548px;overflow:hidden}
body{position:relative;font-family:"Open Sans",Arial,sans-serif;color:var(--ink);background:#3a2a22}
.abs{position:absolute}

/* backdrop */
.backdrop{left:0;top:600px;width:1200px;height:1560px;background:radial-gradient(ellipse at 15% 30%,#6b4a35,#2e1f18 60%),#2e1f18}

/* header */
.topbar{left:0;top:0;width:1200px;height:60px;background:rgba(20,18,17,.92);z-index:3}
.brand{left:110px;top:0;width:124px;height:78px;background:var(--night);display:flex;align-items:flex-end;justify-content:center;padding-bottom:14px;z-index:4}
.brand span{font-family:"Open Sans",sans-serif;font-weight:600;font-size:14px;color:var(--white);white-space:nowrap}
.nav{left:540px;top:22px;display:flex;gap:26px;z-index:4}
.nav a{font-size:11px;font-weight:700;color:var(--white);text-decoration:none;letter-spacing:.5px}
.topcontact{right:120px;top:16px;font-size:10px;color:#ddd;text-align:right;line-height:14px;z-index:4}

/* hero */
.hero{left:0;top:0;width:1200px;height:600px;background:linear-gradient(90deg,#8a5a45 0%,#5a2f24 35%,#3d2620 60%,#6d4a3a 100%)}
.hero-copy{right:130px;top:150px;width:600px;text-align:right;color:var(--white)}
.hero-copy .kicker{font-family:"Playfair Display",serif;font-style:italic;font-size:26px}
.hero-copy h1{font-family:"Roboto Slab",serif;font-weight:700;font-size:40px;line-height:46px;margin-top:4px;text-transform:uppercase;white-space:nowrap}
.hero-copy p{font-size:15px;line-height:20px;margin-top:10px}
.btn{display:inline-block;background:var(--red);color:var(--white);font-size:13px;font-weight:600;border-radius:4px;padding:11px 26px;white-space:nowrap}
.hero-copy .btn{margin-top:22px;margin-right:70px}

/* panel */
.panel{left:140px;top:620px;width:920px;height:1540px;background:var(--white)}
.cats{left:160px;top:632px;display:flex;gap:20px}
.cat{position:relative;width:430px;height:150px}
.cat.food{background:linear-gradient(120deg,#d7c7b0,#a7835e)}
.cat.fruit{background:linear-gradient(120deg,#9aa86a,#c2593c)}
.cat span{position:absolute;left:0;bottom:0;width:100%;padding:6px 12px;background:rgba(0,0,0,.55);color:var(--white);font-family:"Roboto Slab",serif;font-weight:700;font-size:18px}

.section-title{font-family:"Roboto Slab",serif;font-weight:800;font-size:62px;color:var(--red);line-height:64px;white-space:nowrap}
.section-sub{font-family:"Roboto Slab",serif;font-weight:700;font-size:21px;color:var(--grey);line-height:25px;text-transform:uppercase}

.products-title{left:160px;top:800px}
.products-sub{left:160px;top:870px;width:860px}

.grid{left:160px;top:955px;width:880px;display:grid;grid-template-columns:repeat(3,280px);column-gap:20px;row-gap:22px}
.card-img{height:220px}
.card h3{font-family:"Roboto Slab",serif;font-weight:700;font-size:21px;color:var(--red);margin-top:8px}
.card p{font-size:9.5px;line-height:13px;color:#555;margin-top:4px}
.price{font-size:13px;margin-top:6px}
.price b{color:var(--red);font-size:16px}
.card .btn{font-size:11px;padding:5px 12px;margin-top:5px;border-radius:3px}

.about-title{left:160px;top:1760px}
.about-sub{left:160px;top:1830px;width:860px;font-family:"Roboto Slab",serif;font-weight:700;font-size:19px;line-height:24px;color:var(--ink)}
.about-body{left:160px;top:1895px;width:880px;font-size:9.5px;line-height:14px;color:#555}
.about-body p+p{margin-top:10px}
.readmore{left:540px;top:2075px}
.readmore .btn{padding:13px 40px;font-size:14px}

/* footer */
.footer{left:0;top:2160px;width:1200px;height:260px;background:var(--footer)}
.fcol{color:var(--footer-text)}
.fcol h4{font-family:"Roboto Slab",serif;font-weight:700;font-size:17px;color:var(--white);margin-bottom:10px}
.recent{left:160px;top:2180px;width:270px}
.recent .item{display:flex;gap:10px;margin-bottom:10px}
.thumb{width:72px;height:48px;flex:none}
.recent .item p{font-size:9.5px;line-height:13px;color:var(--footer-text)}
.location{left:460px;top:2180px;width:270px;font-size:10px;line-height:15px}
.map{width:240px;height:100px;margin-top:10px;background:linear-gradient(135deg,#e6e1d6,#c9d3c0)}
.news{left:760px;top:2180px;width:280px;font-size:10px;line-height:14px}
.news .field{height:24px;background:var(--white);margin-top:10px;width:240px}
.news .btn{font-size:10px;padding:4px 12px;margin-top:8px;border-radius:3px}
.social{left:760px;top:2320px}
.social .row{display:flex;gap:6px}
.social i{display:block;width:26px;height:26px;background:#5a5654;border-radius:3px}

.callband{left:140px;top:2420px;width:920px;height:90px;background:var(--white);text-align:center;padding-top:16px}
.callband .call{font-size:14px;font-weight:700;color:var(--red)}
.callband p{font-size:9.5px;line-height:13px;color:#666;margin-top:6px}
.bottombar{left:0;top:2510px;width:1200px;height:38px;background:var(--night);color:#bbb;font-size:10px;padding:13px 160px}
</style>
</head>
<body>

<div class="abs backdrop" role="img" aria-label="Dark close-up of chocolate pieces and coffee beans"></div>

<section class="abs hero" role="img" aria-label="Cherry-topped chocolate tart on a table with a cup of tea"></section>
<div class="abs hero-copy">
  <div class="kicker">Love having dairy friends</div>
  <h1>In the family and<br>take caring of him</h1>
  <p>At our shop, fresh pastries are baked every<br>morning by hand with premium ingredients.<br>Drop by and taste one on us.</p>
  <span class="btn">View Our Products ›</span>
</div>

<header>
  <div class="abs topbar"></div>
  <div class="abs brand"><span>Lantern &amp; Plum</span></div>
  <nav class="abs nav"><a>HOME</a><a>ABOUT</a><a>PRODUCT</a><a>GALLERY</a><a>CONTACT</a></nav>
  <div class="abs topcontact">hello@lanternandplum.example<br>(555) 014-2288</div>
</header>

<main>
  <div class="abs panel"></div>

  <div class="abs cats">
    <div class="cat food" role="img" aria-label="Assorted baked food on a table"><span>Food</span></div>
    <div class="cat fruit" role="img" aria-label="Fresh fruits and vegetables"><span>Fruits &amp; Vegetables</span></div>
  </div>

  <h2 class="abs section-title products-title">OUR PRODUCTS</h2>
  <p class="abs section-sub products-sub">We believe that you should not feed your dog anything that you would not eat yourself.</p>

  <div class="abs grid">
    <article class="card">
      <div class="card-img" role="img" aria-label="Layered chocolate cream cake slice" style="background:linear-gradient(160deg,#efe7df,#6b3f2c)"></div>
      <h3>Product Name</h3>
      <p>Our layered cake is baked fresh each morning with imported cocoa, soft cream and a light sponge, finished by hand in small batches for a rich taste.</p>
      <div class="price">Price <b>$ 14.00</b></div>
      <span class="btn">Add To Cart 🛒</span>
    </article>
    <article class="card">
      <div class="card-img" role="img" aria-label="Orange glazed cake with fruit" style="background:linear-gradient(160deg,#f6e4c8,#e07a1c)"></div>
      <h3>Product Name</h3>
      <p>A bright orange glazed cake topped with fresh fruit, made with natural juice and no preservatives, perfect for sharing with family and friends at home.</p>
      <div class="price">Price <b>$ 15.00</b></div>
      <span class="btn">Add To Cart 🛒</span>
    </article>
    <article class="card">
      <div class="card-img" role="img" aria-label="Round cake with white cream swirls" style="background:linear-gradient(160deg,#f4eeec,#c8a9a6)"></div>
      <h3>Product Name</h3>
      <p>A round cream cake with piped swirls and a delicate berry filling, whipped by hand from fresh dairy and baked to order by our award winning chefs.</p>
      <div class="price">Price <b>$ 20.00</b></div>
      <span class="btn">Add To Cart 🛒</span>
    </article>
    <article class="card">
      <div class="card-img" role="img" aria-label="Chocolate mousse cake slice on white" style="background:linear-gradient(160deg,#f2f2f2,#4a2a1d)"></div>
      <h3>Product Name</h3>
      <p>A smooth chocolate mousse slice on a crisp base, made with dark imported chocolate and fresh cream, light enough to enjoy after any meal of the day.</p>
      <div class="price">Price <b>$ 14.00</b></div>
      <span class="btn">Add To Cart 🛒</span>
    </article>
    <article class="card">
      <div class="card-img" role="img" aria-label="Chocolate shaving cake on a plate" style="background:linear-gradient(160deg,#e8ded6,#5a3320)"></div>
      <h3>Product Name</h3>
      <p>A whole cake covered in curled chocolate shavings, layered with ganache and sponge, baked fresh and boxed with care for celebrations and gifts alike.</p>
      <div class="price">Price <b>$ 140.00</b></div>
      <span class="btn">Add To Cart 🛒</span>
    </article>
    <article class="card">
      <div class="card-img" role="img" aria-label="Dark chocolate cake slices on black" style="background:linear-gradient(160deg,#2a1e1a,#6e3b28)"></div>
      <h3>Product Name</h3>
      <p>Dense dark chocolate slices with a glossy top, made from our own hand crafted fillings and premium cocoa, a favourite among our returning guests.</p>
      <div class="price">Price <b>$ 20.00</b></div>
      <span class="btn">Add To Cart 🛒</span>
    </article>
  </div>

  <h2 class="abs section-title about-title">ABOUT US</h2>
  <p class="abs about-sub">Lorem Ipsum passage, used since the 1500s "Lorem ipsum dolor sit amet, consectetur adipiscing elit, sed do eiusmod tempor incid</p>
  <div class="abs about-body">
    <p>We are a premium pastry house making cakes, macarons, cookies and gelato by hand every day. Our recipes are developed by award winning chefs, and we make nearly all of our fillings, creams and doughs ourselves. Every product is freshly baked with imported ingredients and no added preservatives, so each bite tastes the way a pastry should. We sell online to keep prices fair while never cutting corners on quality or care.</p>
    <p>Food safety and cleanliness guide every step in our kitchen, from sourcing to packing. We believe one taste is all it takes, which is why we invite new guests to a free tasting before they order. Most of our customers return again and again, and we look forward to welcoming you to our table soon.</p>
  </div>
  <div class="abs readmore"><span class="btn">Read More</span></div>
</main>

<footer>
  <div class="abs footer"></div>

  <div class="abs fcol recent">
    <h4>Recent Products</h4>
    <div class="item"><div class="thumb" role="img" aria-label="Chocolate cake thumbnail" style="background:#6b3f2c"></div><p>Fresh chocolate cake baked daily with cream and cocoa.</p></div>
    <div class="item"><div class="thumb" role="img" aria-label="Fruit tart thumbnail" style="background:#c9792e"></div><p>Seasonal fruit tart with a buttery crust and glaze.</p></div>
    <div class="item"><div class="thumb" role="img" aria-label="Cream cake thumbnail" style="background:#d9c4bf"></div><p>Light cream cake with berries, made to order.</p></div>
  </div>

  <div class="abs fcol location">
    <h4>Our Location</h4>
    <div>Phone: (555) 014-2288<br>Fax: (555) 014-2290<br>Address: 18 Plum Lane, Suite 4<br>Email: hello@lanternandplum.example</div>
    <div class="map" role="img" aria-label="Street map of the shop location"></div>
  </div>

  <div class="abs fcol news">
    <h4>Newsletter</h4>
    <div>Sign up for news on fresh bakes,<br>tastings and seasonal treats.</div>
    <div class="field"></div>
    <span class="btn">Send</span>
  </div>

  <div class="abs fcol social">
    <h4>Social Connection</h4>
    <div class="row"><i></i><i></i><i></i><i></i><i></i><i></i></div>
  </div>

  <div class="abs callband">
    <div class="call">Call Us Toll Free (555) 014-2288 &amp; 1-(555-014-2299)</div>
    <p>Fresh pastries baked by hand every day with premium ingredients and no preservatives.<br>Book a free tasting today and discover why our guests keep coming back for more.</p>
  </div>

  <div class="abs bottombar">Copyright © 2016 . All Rights Reserved</div>
</footer>

</body>
</html>
```